Executive Performance Review mapped on J-curve

I need to turn an executive company performance review into a visual infographic. The list of accomplishments is grouped into four calendar quarters. Each quarter needs a subtle representation of the season. The four quarters and associated list of accomplishments need to be mapped to a J-curve. - Spreadsheet with accomplishments attached (Throughput)- Sample image of a J-curve. You can google J-curve to see more images.- The title should be "Danela Morsky Year in Review"

Target Market(s)

Board of Directors

Requirements
Nice to have
• This will be presented to a company founder that is an artist and customer experience expert. He is very visual so a nice visual representation of the data will be impactful. He also uses the phrase that you have to live with or work with someone for four seasons before you really know them. This is why I have the seasons mapped to the quarters. The Fall season motif should be gloomy and stormy.

```html
<!DOCTYPE html>
<html lang="en">
<head>
<meta charset="utf-8">
<title>Danela Morsky Year in Review</title>
<link rel="stylesheet" href="https://fonts.googleapis.com/css2?family=Archivo+Black&family=Oswald:wght@600&family=Roboto:wght@400;500;700&display=swap">
<style>
  :root {
    --brand-blue: #0a70c2;
    --ink: #111;
    --grey-text: #6b6b6b;
    --frame: #e4e4e4;
    --summer-a: #0a6cc4; --summer-b: #3a9ad8;
    --fall-a: #1e1f20; --fall-b: #4a4c4e;
    --winter-a: #b4ee3a; --winter-b: #d0f56a;
    --spring-a: #f58a0e; --spring-b: #e06e08;
    --node-summer: #0a70c2; --node-fall: #1f1f1f; --node-winter: #aaff00; --node-spring: #ff7d00;
    --pink: #ff0a7a;
  }
  * { box-sizing: border-box; margin: 0; padding: 0; }
  html, body { width: 1200px; height: 911px; overflow: hidden; background: #fff; }
  body { font-family: "Roboto", Arial, sans-serif; color: var(--ink); }
  .canvas { position: relative; width: 1200px; height: 911px; overflow: hidden; background: #fff; }
  .frame { position: absolute; left: 64px; top: 49px; width: 1076px; height: 817px; border: 5px solid var(--frame); }

  .title { position: absolute; left: 198px; top: 92px; font-family: "Archivo Black", sans-serif; font-size: 64px; line-height: 1; color: var(--brand-blue); letter-spacing: -0.5px; }
  .subtitle { position: absolute; left: 205px; top: 176px; height: 23px; display: flex; align-items: center; }
  .subtitle-mark { width: 34px; height: 23px; background: var(--brand-blue); }
  .subtitle-text { font-weight: 700; font-size: 24px; color: #333; margin-left: 7px; line-height: 1; }
  .subtitle-bar { position: absolute; left: 417px; top: 176px; width: 280px; height: 23px; background: var(--frame); }

  .badge { position: absolute; left: 944px; top: 89px; width: 130px; height: 130px; border-radius: 50%; border: 6px solid var(--pink); background: #fff; display: flex; align-items: center; justify-content: center; }
  .badge-core { width: 101px; height: 101px; border-radius: 50%; background: var(--pink); color: #fff; font-family: "Archivo Black", sans-serif; font-size: 16.5px; line-height: 1.1; text-align: center; display: flex; align-items: center; justify-content: center; }

  .throughput-label { position: absolute; font-family: "Archivo Black", sans-serif; font-size: 9.5px; letter-spacing: 3.2px; color: #6d6d6d; }
  .throughput-label.small { font-size: 7px; letter-spacing: 2.3px; }

  .panel { position: absolute; overflow: hidden; }
  .panel-bg { position: absolute; inset: 0; }
  .panel-body { position: relative; }
  .panel h3 { font-size: 13.5px; font-weight: 700; line-height: 1.05; margin-top: 3px; }
  .panel ul { list-style: none; font-size: 9.2px; line-height: 9.8px; }
  .panel li { position: relative; padding-left: 8px; }
  .panel li::before { content: ""; position: absolute; left: 1px; top: 3px; width: 4.5px; height: 4.5px; border-radius: 50%; background: currentColor; }
  .revenue h3 { font-size: 13.5px; }
  .revenue .amount { font-family: "Roboto", sans-serif; font-weight: 700; font-size: 27px; line-height: 1; }
  .rule { height: 2.5px; background: currentColor; }

  .panel-summer { left: 180px; top: 329px; width: 200px; height: 350px; color: #fff; }
  .panel-summer .panel-bg { background: linear-gradient(170deg, var(--summer-a), var(--summer-b) 55%, var(--summer-a)); }
  .panel-summer .panel-body { padding: 11px 6px 0 18px; }
  .panel-summer h3 + ul { margin-top: 0; }
  .panel-summer .revenue { position: absolute; left: 18px; top: 291px; width: 182px; }
  .panel-summer .revenue .r1 { margin: 10px 0 0 10px; width: 88%; }
  .panel-summer .revenue .amount { text-align: right; padding-right: 22px; margin-top: 1px; }
  .panel-summer .revenue .r2 { margin-left: 58px; width: 112px; }

  .panel-fall { left: 393px; top: 482px; width: 200px; height: 310px; color: #fff; }
  .panel-fall .panel-bg { background: radial-gradient(ellipse at 60% 70%, var(--fall-b), var(--fall-a) 70%); }
  .panel-fall .panel-body { padding: 16px 6px 0 20px; }
  .panel-fall .revenue { margin: 6px 0 0 0; }
  .panel-fall .revenue .r1 { margin: 3px 0 0 -3px; width: 140px; }
  .panel-fall .revenue .amount { margin: 2px 0 0 2px; }
  .panel-fall .revenue .r2 { margin: 2px 0 0 -3px; width: 110px; }

  .panel-winter { left: 606px; top: 224px; width: 183px; height: 341px; color: #111; }
  .panel-winter .panel-bg { background: linear-gradient(160deg, var(--winter-b), var(--winter-a) 60%, #a6e02e); }
  .panel-winter .panel-body { padding: 13px 6px 0 15px; }
  .panel-winter .revenue { margin-top: 5px; }
  .panel-winter .revenue .r1 { margin-top: 2px; width: 118px; }
  .panel-winter .revenue .amount { margin-top: 2px; }
  .panel-winter .revenue .r2 { margin-top: 2px; width: 91px; }

  .panel-spring { left: 801px; top: 321px; width: 171px; height: 314px; color: #111; text-align: right; }
  .panel-spring .panel-bg { background: linear-gradient(200deg, var(--spring-a), #f79a22 45%, var(--spring-b)); }
  .panel-spring .panel-body { padding: 25px 13px 0 6px; }
  .panel-spring li { padding-left: 0; padding-right: 7px; }
  .panel-spring li::before { left: auto; right: 0; }
  .panel-spring .revenue { margin-top: 5px; }
  .panel-spring .revenue .r1 { margin: 6px 0 0 auto; width: 124px; }
  .panel-spring .revenue .amount { margin-top: 1px; }
  .panel-spring .revenue .r2 { margin: 1px 0 0 auto; width: 124px; }

  .curve { position: absolute; left: 0; top: 0; width: 1200px; height: 911px; pointer-events: none; }

  .season { position: absolute; line-height: 0.95; }
  .season .name { font-family: "Oswald", sans-serif; font-weight: 600; font-size: 19px; color: var(--ink); letter-spacing: 0.2px; line-height: 1; }
  .season .quarter, .season .theme { font-weight: 700; font-size: 16.5px; color: var(--grey-text); line-height: 0.95; }
  .season.right { text-align: right; }
  .season-summer { left: 170px; top: 709px; }
  .season-fall { left: 460px; top: 788px; width: 77px; }
  .season-winter { left: 640px; top: 562px; width: 107px; }
  .season-spring { left: 780px; top: 232px; width: 108px; }
</style>
</head>
<body>
<div class="canvas">
  <div class="frame"></div>

  <h1 class="title">Danela Morsky</h1>
  <div class="subtitle"><div class="subtitle-mark"></div><div class="subtitle-text">Year in Review</div></div>
  <div class="subtitle-bar"></div>

  <div class="badge"><div class="badge-core">2020<br>Value<br>Creation</div></div>

  <!-- Summer -->
  <div class="throughput-label" style="left:226px; top:317px;">THROUGHPUT</div>
  <section class="panel panel-summer">
    <div class="panel-bg" role="img" aria-label="Sunny tropical beach with palm trees in blue tones"></div>
    <div class="panel-body">
      <h3>Transitions</h3>
      <ul>
        <li>RO Transition from Ravi &amp; Lena</li>
        <li>Start CR Office Initiative</li>
        <li>Tactical Ops transition from Ravi</li>
        <li>Formalize Exec Team</li>
      </ul>
      <h3 style="margin-top:5px">Biz Architecture</h3>
      <ul>
        <li>Independent Financial Audit</li>
        <li>Organizational Audit - Structure</li>
        <li>Organizational Audit - People</li>
        <li>XF Framework - ESU</li>
        <li>Defined Utilization, Realization, Availability</li>
      </ul>
      <h3 style="margin-top:5px">Strategy</h3>
      <ul>
        <li>Effective Strategy Meeting</li>
        <li>Strategic Themes 2018 - 2020: Stablize, Accelerate, Surge</li>
        <li>Business Drivers: Drive Revenue, Improve Veltrix Experience, Increase Brand Awareness</li>
      </ul>
      <h3 style="margin-top:5px">Sales</h3>
      <ul>
        <li>Fernwell Account Transition</li>
        <li>Alder Account Transition</li>
        <li>2 year Managed Services Engagement Model</li>
      </ul>
    </div>
    <div class="revenue">
      <h3>Revenue / EBITA</h3>
      <div class="rule r1"></div>
      <div class="amount">$000</div>
      <div class="rule r2"></div>
    </div>
  </section>

  <!-- Fall -->
  <div class="throughput-label" style="left:439px; top:471px;">THROUGHPUT</div>
  <section class="panel panel-fall">
    <div class="panel-bg" role="img" aria-label="Gloomy stormy sea with a weathered boat in dark grey tones"></div>
    <div class="panel-body">
      <h3>Biz Architecture</h3>
      <ul>
        <li>XF Framework - Functional<br>Meetings &amp; Scrum of Scrums</li>
        <li>Structured Reorg</li>
        <li>Implemented Reorg</li>
        <li>Quarterly Org Iteration cadence</li>
        <li>Defined Key Hire Plan</li>
        <li>CR Office Operational</li>
        <li>Time Accountability</li>
        <li>Tools ReConfig</li>
        <li>Org Structure v1</li>
      </ul>
      <h3 style="margin-top:6px">Strategy</h3>
      <ul><li>Internal QBR Accountability</li></ul>
      <h3 style="margin-top:6px">Sales</h3>
      <ul>
        <li>Brightmoor QBR</li>
        <li>Fernwell QBR</li>
      </ul>
      <div class="revenue">
        <h3>Revenue / EBITA</h3>
        <div class="rule r1"></div>
        <div class="amount">$000</div>
        <div class="rule r2"></div>
      </div>
    </div>
  </section>

  <!-- Winter -->
  <div class="throughput-label" style="left:648px; top:212px;">THROUGHPUT</div>
  <section class="panel panel-winter">
    <div class="panel-bg" role="img" aria-label="Snowy road through frosted trees in bright green tones"></div>
    <div class="panel-body">
      <h3>Biz Architecture</h3>
      <ul>
        <li>XF Framework - Progress Demos</li>
        <li>Org Structure - COE's</li>
        <li>Stablize Accounting &amp; Finance</li>
        <li>Exec Hiring Process</li>
      </ul>
      <h3 style="margin-top:6px">Key Hires</h3>
      <ul>
        <li>Controller</li>
        <li>Director CX</li>
      </ul>
      <h3 style="margin-top:6px">Strategy</h3>
      <ul>
        <li>Founders removed from front line activity</li>
        <li>Tessel QBR - Goal Setting &amp; Tracking</li>
      </ul>
      <h3 style="margin-top:6px">Sales</h3>
      <ul>
        <li>Alder QBR</li>
        <li>Fernwell QBR</li>
      </ul>
      <div class="revenue">
        <h3>Revenue / EBITA</h3>
        <div class="rule r1"></div>
        <div class="amount">$000</div>
        <div class="rule r2"></div>
      </div>
    </div>
  </section>

  <!-- Spring -->
  <div class="throughput-label small" style="left:903px; top:310px;">THROUGHPUT</div>
  <section class="panel panel-spring">
    <div class="panel-bg" role="img" aria-label="Blooming spring flowers in warm orange tones"></div>
    <div class="panel-body">
      <h3>Biz Architecture</h3>
      <ul>
        <li>Tiered Pricing Pre-Paid<br>Engagement Model</li>
        <li>XF Framework - Ideation Board</li>
        <li>Consulting Levels &amp; Salary<br>Bands</li>
        <li>Roles &amp; Responsibilities</li>
      </ul>
      <h3 style="margin-top:6px">Key Hires</h3>
      <ul>
        <li>Interim HR</li>
        <li>Provisional Client Partner</li>
        <li>Acting Director 1</li>
        <li>Acting Director 2</li>
        <li>Client Partner 1</li>
        <li>Sales Exec 1</li>
      </ul>
      <h3 style="margin-top:6px">Sales</h3>
      <ul>
        <li>Opened Glowhaus Door</li>
        <li>Flipped focus from operationaly<br>run company to sales/marketing<br>driven org</li>
        <li>Northvale Direct</li>
      </ul>
      <div class="revenue">
        <h3>Revenue / EBITA</h3>
        <div class="rule r1"></div>
        <div class="amount">$000</div>
        <div class="rule r2"></div>
      </div>
    </div>
  </section>

  <svg class="curve" viewBox="0 0 1200 911" aria-hidden="true">
    <path d="M224 679 C 280 760, 350 805, 415 802 C 510 798, 575 700, 660 562 L 867 314 L 975 203" fill="none" stroke="#000" stroke-width="10" stroke-linecap="round"/>
    <g>
      <circle cx="224" cy="679" r="26" fill="#000"/><circle cx="224" cy="679" r="22" fill="#fff"/><circle cx="224" cy="679" r="18.5" fill="var(--node-summer)"/>
      <circle cx="473" cy="779" r="26" fill="#000"/><circle cx="473" cy="779" r="22" fill="#fff"/><circle cx="473" cy="779" r="18.5" fill="var(--node-fall)"/>
      <circle cx="660" cy="562" r="26" fill="#000"/><circle cx="660" cy="562" r="22" fill="#fff"/><circle cx="660" cy="562" r="18.5" fill="var(--node-winter)"/>
      <circle cx="867" cy="314" r="26" fill="#000"/><circle cx="867" cy="314" r="22" fill="#fff"/><circle cx="867" cy="314" r="18.5" fill="var(--node-spring)"/>
    </g>
  </svg>

  <div class="season season-summer"><div class="name">SUMMER</div><div class="quarter">Q3 2018</div><div class="theme">Assessment</div></div>
  <div class="season season-fall right"><div class="name">FALL</div><div class="quarter">Q4 2018</div><div class="theme">Stablize</div></div>
  <div class="season season-winter right"><div class="name">WINTER</div><div class="quarter">Q1 2019</div><div class="theme">Stractical</div></div>
  <div class="season season-spring right"><div class="name">SPRING</div><div class="quarter">Q2 2019</div><div class="theme">Strategic</div></div>
</div>
</body>
</html>
```